creating a certificate for our flagship course

Hi,
We need a new certificate for our flagship course called Bright Harbour. We have been running this course for 25 years this year and want to get something special that represents that. We need our logos incorporated and we love to have a compass or Koru incorporated in the certificate. We like something different from your standard certificate, but not too crazy.

The text should say something along the lines of:
This certificate is awarded to ....
For successfully completing and contributing to the three day Bright Harbour programme.

signed:... date:...

to learn a bit more about this course and our company, please check our website. www.hollisvantreeve.co.nz

Thank you!

Target Market(s)

attendees who completed our 3 day programme.

Requirements
Must have
• Both our BH logo and our brand logo. a compass or a koru.
• a 25th year existence something on it.

```html
<!DOCTYPE html>
<html lang="en">
<head>
<meta charset="utf-8">
<title>Bright Harbour Programme Certificate</title>
<link href="https://fonts.googleapis.com/css2?family=Great+Vibes&family=Playfair+Display:wght@400;700&family=Montserrat:wght@700&family=Open+Sans:wght@400&display=swap" rel="stylesheet">
<style>
  :root {
    --navy: #2b2d4e;
    --paper: #ffffff;
    --white: #ffffff;
    --accent-green: #8cc63f;
    --rule: #9a9bb0;
  }
  html, body {
    margin: 0;
    padding: 0;
    overflow: hidden;
    background: var(--paper);
  }
  .certificate {
    position: relative;
    width: 848px;
    height: 1200px;
    background: var(--paper);
    overflow: hidden;
    color: var(--navy);
  }
  .frame-shapes {
    position: absolute;
    inset: 0;
  }
  .brand-block {
    position: absolute;
    left: 284px;
    top: 40px;
    width: 280px;
    text-align: center;
    color: var(--white);
  }
  .brand-mark {
    display: block;
    width: 40px;
    height: 40px;
    margin: 0 auto 14px;
    background: var(--accent-green);
  }
  .brand-name {
    font-family: "Playfair Display", serif;
    font-size: 21px;
    line-height: 1.15;
    letter-spacing: 1px;
    text-transform: uppercase;
    margin: 0;
  }
  .programme-block {
    position: absolute;
    left: 284px;
    top: 214px;
    width: 280px;
    display: flex;
    align-items: center;
    justify-content: center;
    gap: 12px;
    color: var(--white);
  }
  .programme-mark {
    width: 52px;
    height: 52px;
    border-radius: 8px;
    background: var(--accent-green);
  }
  .programme-name {
    font-family: "Open Sans", sans-serif;
    font-size: 17px;
  }
  .title {
    position: absolute;
    left: 0;
    width: 848px;
    top: 350px;
    margin: 0;
    text-align: center;
    font-family: "Great Vibes", cursive;
    font-weight: 400;
    font-size: 158px;
    line-height: 1;
    color: var(--navy);
  }
  .awarded-to {
    position: absolute;
    left: 0;
    width: 848px;
    top: 540px;
    margin: 0;
    text-align: center;
    font-family: "Playfair Display", serif;
    font-weight: 700;
    font-size: 28px;
    letter-spacing: 1px;
    text-transform: uppercase;
  }
  .recipient {
    position: absolute;
    left: 0;
    width: 848px;
    top: 596px;
    margin: 0;
    text-align: center;
    font-family: "Great Vibes", cursive;
    font-size: 88px;
    line-height: 1;
  }
  .achievement {
    position: absolute;
    left: 40px;
    width: 768px;
    top: 756px;
    margin: 0;
    text-align: center;
    font-family: "Montserrat", sans-serif;
    font-weight: 700;
    font-size: 33px;
    line-height: 1.3;
    letter-spacing: 2px;
    text-transform: uppercase;
  }
  .place-date {
    position: absolute;
    left: 62px;
    top: 1040px;
    margin: 0;
    font-family: "Open Sans", sans-serif;
    font-size: 16px;
    line-height: 1.5;
  }
  .signature {
    position: absolute;
    left: 640px;
    top: 1040px;
    width: 150px;
    margin: 0;
    font-family: "Open Sans", sans-serif;
    font-size: 16px;
  }
  .signature-line {
    display: block;
    margin-top: 44px;
    height: 1px;
    background: var(--rule);
  }
  .anniversary {
    position: absolute;
    left: 324px;
    top: 1030px;
    width: 200px;
    text-align: center;
    color: var(--white);
  }
  .anniversary-number {
    display: block;
    font-family: "Playfair Display", serif;
    font-weight: 700;
    font-size: 84px;
    line-height: 1;
  }
  .anniversary-word {
    display: block;
    margin-top: -12px;
    font-family: "Great Vibes", cursive;
    font-size: 36px;
  }
</style>
</head>
<body>
<main class="certificate">
  <svg class="frame-shapes" width="848" height="1200" viewBox="0 0 848 1200" aria-hidden="true">
    <path d="M283 0 H565 V200 A141 141 0 0 1 283 200 Z" fill="var(--navy)"/>
    <path d="M272 0 V200 A152 152 0 0 0 576 200 V0" fill="none" stroke="var(--navy)" stroke-width="1.5"/>
    <path d="M150 706 Q424 700 698 706 Q424 712 150 706 Z" fill="var(--navy)"/>
    <line x1="310" y1="962" x2="538" y2="962" stroke="var(--navy)" stroke-width="2"/>
    <path d="M311 1200 V1118 A113 113 0 0 1 537 1118 V1200 Z" fill="var(--navy)"/>
    <path d="M300 1200 V1118 A124 124 0 0 1 548 1118 V1200" fill="none" stroke="var(--navy)" stroke-width="1.5"/>
  </svg>

  <div class="brand-block">
    <span class="brand-mark"></span>
    <p class="brand-name">Hollis Van Treeve<br>&amp; Associates</p>
  </div>

  <div class="programme-block">
    <span class="programme-mark"></span>
    <span class="programme-name">Bright Harbour</span>
  </div>

  <h1 class="title">Certificate</h1>
  <p class="awarded-to">This certificate is awarded to</p>
  <p class="recipient">Daniel Moore</p>
  <p class="achievement">For successfully completing<br>and contributing to the<br>three day Bright Harbour<br>programme</p>

  <p class="place-date">Dunedin,<br>30.4.2016.</p>

  <div class="anniversary">
    <span class="anniversary-number">25</span>
    <span class="anniversary-word">years</span>
  </div>

  <p class="signature">Chairman<span class="signature-line"></span></p>
</main>
</body>
</html>
```